!! Innovative new tea company needs packaging design !!

** NB. We need this project as a starting point for our company. We would like to/ intend to have an ongoing relationship with the designer to add to/ change and develop the design in the future on freelance basis pending available workload.

We are in the process of creating a range of functional wellness drinks based on green tea - company name k~. We will have a range of drinks based on green tea attributed to functional effects - boost, detox, immunity etc. Aim of the company is to create a healthy, modern, vibrant company that offers a range of drinks that offer healthy wellness properties, in great tasting fruit flavours.

We need packaging design for the boxes, initially for tea bags. dimensions will be Length – 12cm, Width – 6.75cm, Height – 7.75cm ( please note this means that the box will be TALL / UPRIGHT STANDING)

The brand name is k~ ( to represent green tea + other ingredients / effects). Four initial tea's will be produced that we need to show packaging for :

k~ boost ( rasberry & pomegranite flavour )
k~ immunity ( orange & blueberry )
k~ detox ( apple & blackcurrant )
k~ multi vitamin ( lemon & peach )

We have had the below central brand logo and individual tea logo edits produced already, attached below.

*****Please note we intend the 4 packages to be the same consistent design - only change is on the title of each. For that reason we ONLY REQUEST TO SEE ONE DESIGN ON ONE PRODUCT from a designer to agree on format. Once agreed we will then request you give us the other 3 on agreed format ******

We are aiming to be a very young, vibrant company aiming at the 20 - 40 health conscious consumer. Were taking inspiration from companies like Quillow smoothies and leaf owls and want branding to be in line with those themes.PLEASE LOOK THIS UP TO UNDERSTAND. We need box designs to be completed. Ideally building on the below designs weve had commissioned. However, if a better suggestion on the logo , or a tweak to these will improve the design then we are very much open to it.

Packaging must be, clear white background and bold colors along the line of each flavour teas colour ( ie red for boost, yellow multi vitamin etc). We would ideally like the top and one side ( ONLY ) of the box to be coloured background ( matching the drink colour ). We are wanting simple and clear design FAIRLY MINIMALIST to convey the point of the brand to be simple clear and healthy ingredients. At the same time it must clearly stand out on a shelf. Lighthearted and not too serious, ideally simple, fun illustrated drawings ( ideally outlines/very simple drawings) of the fruit aligned to each flavour and any other branding / mascot logo design that you can suggest.

Also possible cartoon/simple illustration tea leaf somewhere on the box.

We need packaging for the 4 teas - 1 consistent design and theme, with only changes to color and a few illustrations per box.

Please note - We want text font to be funky, friendly, soft - various sizes on the text on the boxes - NOT everything the same size and generic font.

text to go on the box

( front of box):

- main t+boost/immunity etc logo
.(tagline underneath) Wellness drinks

- * Green tea with vitamins drink

- * Natural Ceylon green tea with added vitamins and herbs to give you the best start to your day.

- * 5 reasons to drink this!!
100% natural ingredients
x% of your RDA of x
x mg of antioxidants to keep your heart healthy.
Naturally sweet taste
only x calories per cup!

(side of box)

Ingredients

We use only the finest hand picked ceylon green tea and mix it with natural fruit pieces, a hint of natural flavouring as our base. We add the goodness of burdock root and echinacea to help build your body's defenses and sweeten it with a dash of the south american stevia leaf to give a great tasting drink that will do you some good!

( side of box )

Nutrition Facts

Serving Size: 1 tea bag (4g)

Makes: 8 fl. oz.

Servings Per Container: 25

Amount Per Serving
Calories 0

% Daily Value*
Total Fat 0g
0%
Sodium 0mg
5%
Total Carb. 0g
0%
Sugars 10g
Protein 0g

* Percent Daily Values are based on a 2,000 calorie diet.

The above is how we forsee the packaging for now. However - anything that you can reccommend that is innovative to help us stand out to a young , trendy audience will be welcome.

Please message with any questions or comments.
Updates

Dear All - Please note - we have updated the brief with the packaging die line for your reference. Please note the box will be upstanding so designs should accomodate for a tall box.

Dear All - To reiterate key points of the brief - We request the deign to be stand out here. Majority white background with splashes/swirls/blotches of colour ( whatever design suggested ).Further to that, illustrations ( drawings - not pictures ) of fruit / tea leaves to stay in line with young, funky image. 

Overall theme is young, bright and modern - we need the packaging to reflect this. Not just standard text font and background colouring.
Any more clarity needed please contact us. 

Reason: Dear All We have increased the budget for this project and extended the deadline by additional 7 days. To date we have not received the designs we are happy with so want to give all added time to revise - follow the brief - and resubmit. Due to quality of designs received so far - we will not guarantee payment yet - HOWEVER - Intention is to get this completed for the business by next week latest- for that reason, as soon as someone has submitted a design that is at least along the right lines - we will then move to guarantee payment. Please also note - we intend to / hope to work with the designer directly on ongoing projects for the company so want a good - long term relationship from this. Good luck and please contact us if any more information needed. Regards

Dear all

Please can we request that for the sides of the box with a white background - text is in a green colour ( same shade as the original k~ logo green ). We would like this to be our standard font colour against white background. 

Obviously, please add colour where you see fit but we want a clean , consistent font across the boxes and eventually our web site. 

For the coloured backgrounds of the side and top - will leave up to you whatever colour font looks best. 

Reason: Deadline extended to provide some more feedback to designers. No decision yet made.

Target Market(s)

Young, health conscious individuals.

Industry/Entity Type

It Company

```html
<!DOCTYPE html>
<html lang="en">
<head>
<meta charset="utf-8">
<title>k~ multi vitamin – Lemon &amp; Peach box dieline</title>
<link rel="stylesheet" href="https://fonts.googleapis.com/css2?family=PT+Sans:wght@400;700&family=Rye&display=swap">
<style>
  :root {
    --ink: #111111;
    --body: #1c1c1c;
    --brand-green: #5cc21c;
    --grey: #9a9a9a;
    --pink: #ff2c6f;
    --yellow-green: #c6f400;
    --amber: #e2a52a;
    --headline: #f2462a;
    --paper: #ffffff;
  }
  * { box-sizing: border-box; margin: 0; padding: 0; }
  html, body { width: 1200px; height: 1102px; overflow: hidden; background: var(--paper); }
  .dieline { position: relative; width: 1200px; height: 1102px; font-family: "PT Sans", Arial, sans-serif; color: var(--body); }
  .dieline-lines { position: absolute; inset: 0; }

  .panel-fill { position: absolute; }
  .ingredients-side { left: 594px; top: 316px; width: 306px; height: 475px;
    background: linear-gradient(to bottom, var(--pink) 0%, var(--amber) 50%, var(--yellow-green) 100%); }
  .top-brand-band { left: 900px; top: 316px; width: 268px; height: 139px; background: var(--grey); }
  .top-info { left: 900px; top: 455px; width: 268px; height: 336px;
    background: linear-gradient(to bottom, var(--yellow-green) 0%, var(--amber) 40%, var(--pink) 100%); }

  /* product name block: one font, one weight, one colour */
  .product-name { position: absolute; width: 262px; font-family: "PT Sans", Arial, sans-serif; font-weight: 700;
    color: var(--brand-green); line-height: 1.15; white-space: nowrap; }
  .product-name .line-main { font-size: 26px; }
  .product-name .line-flavour { font-size: 24px; }
  .product-name.flipped { transform: rotate(180deg); text-align: left; }
  .top-band-name { left: 910px; top: 350px; color: #e9ff5a; }
  .top-flap-name { left: 336px; top: 18px; text-align: right; }
  .bottom-flap-name { left: 336px; top: 996px; text-align: right; }

  .rotated { position: absolute; width: 475px; height: 307px; transform: rotate(90deg); transform-origin: center; }
  .nutrition-panel { left: -65px; top: 400px; }
  .ingredients-panel { left: 509.5px; top: 400px; }

  .nutrition-panel .product-name { left: 90px; top: 20px; }
  .nutrition-facts { position: absolute; left: 4px; top: 122px; font-size: 14px; line-height: 20px; }
  .daily-values { position: absolute; left: 356px; top: 82px; font-size: 14px; line-height: 20px; }
  .footnote { position: absolute; left: 4px; top: 282px; font-size: 14px; }

  .ingredients-copy { position: absolute; left: 14px; top: 44px; width: 440px; font-size: 14.4px; line-height: 20.5px; }

  .wellness-title { position: absolute; left: 910px; top: 462px; font-family: "Rye", Georgia, serif; font-size: 24px; font-weight: 400; color: var(--headline); white-space: nowrap; }
  .reasons { position: absolute; left: 905px; top: 523px; width: 262px; font-size: 14.6px; line-height: 20.2px; }
  .reasons p.gap { margin-top: 3px; }
  .reasons .indent { padding-left: 4px; }

  .face-label { position: absolute; font-weight: 700; font-size: 25px; color: var(--ink); }
</style>
</head>
<body>
<main class="dieline">
  <svg class="dieline-lines" width="1200" height="1102" viewBox="0 0 1200 1102" aria-hidden="true">
    <g fill="none" stroke="#111" stroke-width="1.4">
      <rect x="4.5" y="301.5" width="1183" height="504"/>
      <rect x="19.5" y="316.5" width="307" height="475"/>
      <line x1="326.5" y1="316" x2="326.5" y2="791"/>
      <line x1="594.5" y1="316" x2="594.5" y2="791"/>
      <rect x="311.5" y="4.5" width="295" height="307"/>
      <rect x="326.5" y="9.5" width="268" height="307"/>
      <rect x="311.5" y="791.5" width="295" height="307"/>
      <rect x="326.5" y="791.5" width="268" height="302"/>
    </g>
  </svg>

  <div class="panel-fill ingredients-side"></div>
  <div class="panel-fill top-brand-band"></div>
  <div class="panel-fill top-info"></div>

  <div class="product-name flipped top-flap-name">
    <div class="line-main">k~ multi vitamin</div><div class="line-flavour">Lemon &amp; Peach</div>
  </div>
  <div class="product-name flipped bottom-flap-name">
    <div class="line-main">k~ multi vitamin</div><div class="line-flavour">Lemon &amp; Peach</div>
  </div>

  <section class="rotated nutrition-panel">
    <div class="product-name">
      <div class="line-main">k~ multi vitamin</div><div class="line-flavour">Lemon &amp; Peach</div>
    </div>
    <div class="nutrition-facts">
      <p>Nutrition Facts</p>
      <p>Serving Size: 1 tea bag (4g)</p>
      <p>Makes: 8 fl. oz.</p>
      <p>Servings Per Container: 25</p>
      <p>Amount Per Serving</p>
      <p>Calories 0</p>
    </div>
    <div class="daily-values">
      <p>% Daily Value*</p>
      <p>Total Fat 0g</p>
      <p>0%</p>
      <p>Sodium 0mg</p>
      <p>5%</p>
      <p>Total Carb. 0g</p>
      <p>0%</p>
      <p>Sugars 10g</p>
      <p>Protein 0g</p>
    </div>
    <p class="footnote">* Percent Daily Values are based on a 2,000 calorie diet.</p>
  </section>

  <section class="rotated ingredients-panel">
    <p class="ingredients-copy">We use only the finest hand picked ceylon green tea and mix it with natural fruit pieces, a hint of natural flavouring as our base. We add the goodness of burdock root and echinacea to help build your body's defenses and sweeten it with a dash of the south american stevia leaf to give a great tasting drink that will do you some good!</p>
  </section>

  <div class="product-name top-band-name">
    <div class="line-main">k~ multi vitamin</div><div class="line-flavour">Lemon &amp; Peach</div>
  </div>

  <h2 class="wellness-title">WELLNESS DRINKS</h2>
  <div class="reasons">
    <p>* Natural Ceylon green tea with added vitamins and herbs to give you the best <span class="indent">start to your day.</span></p>
    <p class="gap">* 5 reasons to drink this!!</p>
    <p>100% natural ingredients</p>
    <p>x% of your RDA of x</p>
    <p>x mg of antioxidants to keep your<br>heart healthy.</p>
    <p>Naturally sweet taste</p>
    <p>only x calories per cup!</p>
  </div>

  <span class="face-label" style="left:139px;top:801px;">side</span>
  <span class="face-label" style="left:399px;top:808px;">bottom</span>
  <span class="face-label" style="left:708px;top:807px;">side</span>
  <span class="face-label" style="left:1018px;top:813px;">Top</span>
</main>
</body>
</html>
```